Loft Conversion Company Website

Home page and information page design required
This is a redsign of an existing website
http://www.gablenest.example

PLATFORM
Wordpress

SERVICES
Loft Conversions
Extensions
General Building Projects

COMPETITION
Meridian Attics - meridianattics.example
Kestrel Eaves - kestreleaves.example
Dominic Harwell - dominicharwell.example

COMPANY LOGO
Take from the exiting site

COLOURS:

- Blue
- Silver
- White

STRAPLINE:
Loft Conversion Specialists

ACCREDITATIONS / LOGOS:
QTA
WPR OLV
Plover
HSD
Society of Proven Artisans
Skarn
Flue Sure

PLUGINS:
Gallery

PAGES:
Home
London Loft Conversions
- attic loft conversion
- north london loft conversions
- bungalow loft conversion
- dormer loft conversion
- loft conversions prices
- convert a loft
Technical Information
- Structural stability
- Fire safety
- Sound insulation
- Ventilation of rooms and roofs
- Sanitary facilities and drainage
- Stairs and guarding
- Thermal insulation
Gallery
- Case Studies
Testimonials
Contact Us

LOCATION(S):
London -

take correct contact info from the existing site and any pictures you wish to use

Target Market(s)

Families
Home Owners
Developers

male and female 20-65

Industry/Entity Type

Construction

Number of Pages Required

2 pages

Requirements
Must have
• Please take a look at the wireframe, the website must be very visual letting the pictures sell the product, must be classy and almost like a showroom

```html
<!DOCTYPE html>
<html lang="en">
<head>
<meta charset="utf-8">
<title>GableNest – Loft Conversion Specialists</title>
<link href="https://fonts.googleapis.com/css2?family=Arimo:ital,wght@0,400;0,700;1,400&display=swap" rel="stylesheet">
<style>
:root{
  --navy:#0e3a6c;
  --navy-2:#1c5797;
  --blue:#1d5b9b;
  --heading:#1a5a9a;
  --band-top:#3b7bb6;
  --band-bot:#17508b;
  --band-text:#d3e3f3;
  --silver-1:#fafafa;
  --silver-2:#d9d9d9;
  --grey-text:#555;
  --body-text:#3a3a3a;
  --rule:#d6d6d6;
  --white:#fff;
}
*{box-sizing:border-box;margin:0;padding:0}
html,body{width:1200px;height:2954px;overflow:hidden}
body{font-family:"Arimo",Arial,sans-serif;color:var(--body-text);background:var(--white);font-size:12px}
.wrap{position:relative;width:895px;margin-left:152px;height:100%}

/* header */
.site-header{height:115px;background:linear-gradient(180deg,var(--navy) 0%,var(--navy-2) 100%)}
.brand{position:absolute;left:0;top:30px;display:flex;align-items:center;gap:14px}
.brand-mark{width:52px;height:52px;background:var(--white)}
.brand-name{color:var(--white);font-weight:700;font-size:32px;letter-spacing:-.5px}
.callout{position:absolute;right:0;top:28px;color:var(--white);text-align:left;font-size:21px;line-height:27px}
.callout b{font-size:27px}

/* nav */
.main-nav{height:53px;background:linear-gradient(180deg,var(--silver-1),var(--silver-2));border-bottom:1px solid #bbb}
.main-nav ul{list-style:none;display:flex;height:53px;position:absolute;left:0;right:0;justify-content:space-between}
.main-nav li{display:flex;align-items:center;padding:0 2px;font-size:12.5px;font-weight:700;color:var(--grey-text);text-transform:uppercase}
.main-nav li.active{background:var(--blue);color:var(--white);padding:0 19px}
.dropdown{position:absolute;left:54px;top:53px;width:225px;background:#efefef;padding:6px 0 4px;z-index:3;box-shadow:0 1px 2px rgba(0,0,0,.15)}
.dropdown div{font-size:12.5px;color:#333;padding:0 21px;line-height:27px}

/* hero */
.hero{height:352px;background:linear-gradient(90deg,#cfcfcf 0%,#f2f2f2 20%,#f2f2f2 80%,#cfcfcf 100%)}
.slide{position:absolute;left:0;top:31px;width:895px;height:312px;border:5px solid var(--navy);overflow:hidden}
.slide .photo{position:absolute;inset:0;background:linear-gradient(160deg,#8a8d94 0%,#d8d2c8 40%,#efeae2 60%,#2b2b33 100%)}
.slide .caption{position:absolute;left:0;right:0;bottom:0;height:88px;background:rgba(20,20,30,.55);color:var(--white);font-size:31px;padding:26px 40px}
.slide .caption b{font-weight:700}
.arrow{position:absolute;top:169px;width:35px;height:35px}
.arrow.prev{left:-52px}.arrow.next{right:-52px}

/* badges */
.badges{height:80px}
.badges .row{position:absolute;left:0;right:0;top:3px;height:70px;border-top:1px solid var(--rule);border-bottom:1px solid var(--rule);display:flex;justify-content:space-around;align-items:center}
.badge{width:44px;height:44px;background:#b9c3cd}
.badge.round{border-radius:50%}
.badge.wide{width:78px;height:28px;background:#c9c9c9}

/* three column content */
.intro{height:340px}
.col{position:absolute;top:36px;width:272px}
.col.c1{left:0}.col.c2{left:312px}.col.c3{left:625px}
h2.sec{font-size:19.5px;font-weight:700;color:var(--heading);text-transform:uppercase;padding-bottom:7px;border-bottom:2px solid var(--rule);margin-bottom:10px;white-space:nowrap}
h2.sec span{font-weight:400;color:var(--grey-text)}
.client-photo{position:relative;width:272px;height:115px;border:3px solid var(--navy);background:linear-gradient(180deg,#7ea7d3 0%,#b6cde6 35%,#9a4a38 60%,#6f6a64 100%);overflow:hidden}
.ribbon{position:absolute;right:-26px;top:16px;width:110px;height:20px;background:var(--blue);color:var(--white);font-size:9px;font-weight:700;text-align:center;line-height:20px;transform:rotate(45deg)}
.col p{font-size:12px;line-height:17.6px;color:#444}
.client-quote{margin:14px 10px 0}
.client-sig{font-weight:700;margin:16px 10px 0;font-size:12px}
.seal{float:left;width:112px;height:112px;border-radius:50%;background:radial-gradient(circle,#f6d64a 0%,#d9a812 70%,#b88a08 100%);margin:2px 12px 4px 10px}
.btn{display:inline-block;width:124px;height:27px;border-radius:14px;background:linear-gradient(180deg,#fff,#d8d8d8);border:1px solid #bdbdbd;box-shadow:1px 1px 2px rgba(0,0,0,.2);text-align:center;line-height:25px;font-size:12px;font-weight:700;color:#666;text-transform:uppercase}
.field{height:31px;border:1px solid #cfcfcf;background:#f7f7f7;margin:5px 10px 6px;font-size:12px;color:#444;padding:8px 10px}
.field.tall{height:83px}
.btn.small{width:94px}

/* blue band */
.band{height:304px;background:linear-gradient(180deg,var(--band-top),var(--band-bot));border-top:2px solid #6a9ccc}
.band .col{top:28px}
.band h2.sec{color:var(--white);border-bottom:1px solid rgba(255,255,255,.25);font-size:19px}
.band h2.sec span{color:var(--white);font-weight:700}
.band h2.sec em{font-style:normal;font-weight:400}
.band p{color:var(--band-text)}
.thumb{float:left;width:82px;height:82px;border:2px solid #0f3a68;background:linear-gradient(160deg,#3f6b3a,#8a6a3c 60%,#4a3420);margin:4px 10px 4px 10px}
.van{float:left;width:122px;height:78px;margin:4px 10px 2px 10px;background:linear-gradient(180deg,#f4f6f8,#b8c2cc)}
.band .btn{margin:10px 0 0 7px}
.contact-body{position:relative;padding-left:86px}
.phone-ic{position:absolute;left:4px;top:6px;width:70px;height:112px;background:linear-gradient(180deg,#33475e,#1b2a3c);border-radius:6px}
.contact-body h3{color:var(--white);font-size:16px;font-weight:700;margin:12px 0 14px}
.contact-body p{line-height:17.6px}
.contact-body .em{color:var(--white);font-weight:700;margin-top:12px}
.contact-body a{color:var(--white);text-decoration:underline}

/* footer */
.site-footer{height:115px}
.footer-links{position:absolute;top:19px;left:1px;font-size:12.5px;font-weight:700;color:var(--heading);text-transform:uppercase}
.footer-links i{font-style:normal;color:#666;font-weight:400;margin:0 4px}
.copy{position:absolute;top:37px;left:0;font-size:12px;color:#444}
.site-footer.short{height:82px}

/* page two */
.banner-zone{height:205px;background:linear-gradient(90deg,#cfcfcf 0%,#f0f0f0 20%,#f0f0f0 80%,#cfcfcf 100%)}
.banner{position:absolute;left:0;top:31px;width:895px;height:168px;border:5px solid var(--navy);overflow:hidden}
.banner .photo{position:absolute;inset:0;background:linear-gradient(90deg,#e9e4dc 0%,#d8d2c7 25%,#bfa869 45%,#6c8fbf 65%,#b8cde6 100%)}
.banner .caption{position:absolute;left:0;right:0;bottom:0;height:65px;background:rgba(40,40,50,.6);color:var(--white);font-size:32px;padding:15px 0 0 250px}
.banner .caption b{color:#8cc0f0}
.crumbs{height:30px}
.crumbs .line{position:absolute;left:0;right:0;top:0;height:30px;border-bottom:1px solid var(--rule);padding:10px 11px;font-size:11px;color:#777}
.crumbs b{color:var(--heading)}
.article{height:805px}
.main-col{position:absolute;left:0;top:34px;width:583px}
.side-col{position:absolute;left:625px;top:34px;width:270px}
.main-col h2.sec{font-size:21px}
.main-col h4{font-size:12px;font-weight:700;color:#333;line-height:17.6px;margin:18px 0 17px}
.main-col h4.first{margin-top:16px;max-width:540px}
.main-col p{font-size:12px;line-height:17.6px;color:#444;margin-bottom:17px}
.main-col a{color:var(--heading);text-decoration:underline}
.main-col ul{list-style:none;margin:-3px 0 17px 30px}
.main-col li{font-size:12px;line-height:20.8px;color:#444}
.main-col li::before{content:"* "}
.lead p{width:420px}
.quote-disc{position:absolute;right:0;top:106px;width:150px;height:150px;border-radius:50%;background:radial-gradient(circle at 40% 35%,#2d72b8,#134a86);color:var(--white);text-align:center;font-size:21px;line-height:25px;padding-top:24px;box-shadow:0 14px 10px -10px rgba(0,0,0,.35)}
.quote-disc b{color:#ff3b2f;font-weight:700}
.testi{padding:0 20px 0 22px;margin-top:16px}
.testi q{display:block;font-style:italic;font-size:12px;line-height:15px;color:#444;quotes:"‘" "’"}
.testi .who{font-weight:700;font-size:12px;margin:14px 0 28px}
.testi .who.last{margin-bottom:24px}
</style>
</head>
<body>

<!-- ================= HOME ================= -->
<header class="site-header">
  <div class="wrap">
    <div class="brand"><span class="brand-mark"></span><span class="brand-name">GableNest</span></div>
    <div class="callout">CALL: <b>020 7946 0321</b><br>Loft Conversion Specialists</div>
  </div>
</header>
<nav class="main-nav">
  <div class="wrap">
    <ul>
      <li>Home</li><li class="active">London Loft Conversions</li><li>Technical Information</li><li>Gallery</li><li>Testimonials</li><li>Contact Us</li><li>Location</li>
    </ul>
    <div class="dropdown">
      <div>Attic Loft Conversion</div><div>North London Loft Conversions</div><div>Bungalow Loft Conversion</div><div>Dormer Loft Conversion</div><div>Loft Conversions Prices</div><div>Convert a Loft</div>
    </div>
  </div>
</nav>
<section class="hero">
  <div class="wrap">
    <svg class="arrow prev" viewBox="0 0 35 35" aria-hidden="true"><circle cx="17.5" cy="17.5" r="16" fill="#fff" stroke="#bbb"/><path d="M20 10l-8 7.5 8 7.5" fill="none" stroke="#1d5b9b" stroke-width="3.5"/></svg>
    <div class="slide">
      <div class="photo" role="img" aria-label="Photograph of a finished loft bedroom with a bed, chest of drawers and wicker baskets"></div>
      <div class="caption"><b>FREE LOFT CONVERSION</b> SURVEYS</div>
    </div>
    <svg class="arrow next" viewBox="0 0 35 35" aria-hidden="true"><circle cx="17.5" cy="17.5" r="16" fill="#fff" stroke="#bbb"/><path d="M15 10l8 7.5-8 7.5" fill="none" stroke="#1d5b9b" stroke-width="3.5"/></svg>
  </div>
</section>
<section class="badges">
  <div class="wrap">
    <div class="row" aria-label="Accreditations">
      <span class="badge" role="img" aria-label="QTA badge"></span>
      <span class="badge wide" role="img" aria-label="WPR OLV badge"></span>
      <span class="badge round" role="img" aria-label="Plover badge"></span>
      <span class="badge" role="img" aria-label="QTA member badge"></span>
      <span class="badge round" role="img" aria-label="HSD badge"></span>
      <span class="badge round" role="img" aria-label="Society of Proven Artisans badge"></span>
      <span class="badge wide" role="img" aria-label="Skarn badge"></span>
    </div>
  </div>
</section>
<section class="intro">
  <div class="wrap">
    <div class="col c1">
      <div class="client-photo" role="img" aria-label="Photograph of a brick house with a completed loft conversion"><span class="ribbon">LEARN MORE</span></div>
      <h2 class="sec" style="margin:10px 10px 14px">Our Clients <span>Home</span></h2>
      <p class="client-quote">“Lorem ipsum dolor sit amet, consectetur adipiscing elit. Proin eget neque sapien. Vivamus tincidunt lectus sit amet nunc convallis et luctus mi posuere. ”</p>
      <p class="client-sig">- John Doe, North Londo</p>
    </div>
    <div class="col c2">
      <h2 class="sec">10 Years <span>Guarantee</span></h2>
      <div class="seal" role="img" aria-label="Gold 100% satisfaction guaranteed seal"></div>
      <p>Lorem ipsum dolor sit amet, consectetur adipiscing elit. Proin eget neque sapien. Vivamus tincidunt lectus sit amet nunc convallis et luctus mi posuere. Nunc varius pulvinar mauris, nec mattis ipsum varius a. Aliquam ac magna ligula. Nulla convallis accumsan rutrum. Nulla sollicitudin aucto.</p>
      <div style="margin:14px 0 0 10px"><span class="btn">Read More</span></div>
    </div>
    <div class="col c3">
      <h2 class="sec">Free <span>Survey</span></h2>
      <div class="field">Name</div>
      <div class="field tall">Address</div>
      <div class="field">Email</div>
      <div class="field">Phone</div>
      <div style="margin:9px 0 0 10px"><span class="btn small">Submit</span></div>
    </div>
  </div>
</section>
<section class="band">
  <div class="wrap">
    <div class="col c1">
      <h2 class="sec"><span>Visit Our</span> <em>Showroom</em></h2>
      <div class="thumb" role="img" aria-label="Photograph of a dining room showroom"></div>
      <p>Lorem ipsum dolor sit amet, consectetur adipiscing elit. Proin eget neque sapien. Vivamus tincidunt lectus sit amet nunc convallis et luctus mi posuere. Nunc varius pulvinar mauris, nec mattis ipsum varius a. Aliquam ac magna ligula. Nulla convallis accumsan rutrum.</p>
      <span class="btn">Read More</span>
    </div>
    <div class="col c2">
      <h2 class="sec"><em>Unrivelled</em> <span>After Support</span></h2>
      <div class="van" role="img" aria-label="Illustration of a white service van"></div>
      <p>Lorem ipsum dolor sit amet, consectetur adipiscing elit. Proin eget neque sapien. Vivamus tincidunt lectus sit amet nunc convallis et luctus mi posuere. Nunc varius pulvinar mauris, nec mattis ipsum varius a. Aliquam ac magna ligula.</p>
      <span class="btn">Read More</span>
    </div>
    <div class="col c3">
      <h2 class="sec"><span>Contact</span> <em>Information</em></h2>
      <div class="contact-body">
        <div class="phone-ic" role="img" aria-label="Illustration of a telephone handset with coiled cord"></div>
        <h3>GableNest</h3>
        <p>18 Larkfield Road<br>Enfield<br>Middlesex<br>EN2 9QX</p>
        <p class="em">Email us @</p>
        <p><a>sales@gablenest.example</a><br><a>aftersales@gablenest.example</a></p>
      </div>
    </div>
  </div>
</section>
<footer class="site-footer">
  <div class="wrap">
    <div class="footer-links">Home<i>|</i>Technical Information<i>|</i>Gallery<i>|</i>Testimonials<i>|</i>Contact Us<i>|</i>Location</div>
    <div class="copy">© 2010 GableNest. All rights reserved.</div>
  </div>
</footer>

<!-- ================= LONDON LOFT CONVERSIONS ================= -->
<header class="site-header">
  <div class="wrap">
    <div class="brand"><span class="brand-mark"></span><span class="brand-name">GableNest</span></div>
    <div class="callout">CALL: <b>020 7946 0321</b><br>Loft Conversion Specialists</div>
  </div>
</header>
<nav class="main-nav">
  <div class="wrap">
    <ul>
      <li>Home</li><li class="active">London Loft Conversions</li><li>Technical Information</li><li>Gallery</li><li>Testimonials</li><li>Contact Us</li><li>Location</li>
    </ul>
  </div>
</nav>
<section class="banner-zone">
  <div class="wrap">
    <div class="banner">
      <div class="photo" role="img" aria-label="Photograph of a smiling homeowner in a bright loft room under a roof window"></div>
      <div class="caption"><b>QUALITY</b> CONVERSIONS</div>
    </div>
  </div>
</section>
<div class="crumbs"><div class="wrap"><div class="line">HOME &gt; <b>LONDON LOFT CONVERSIONS</b></div></div></div>
<section class="article">
  <div class="wrap">
    <div class="main-col">
      <h2 class="sec">London Loft <span>Conversions</span></h2>
      <h4 class="first">London Loft Conversions in and around North London, Central London, West End and surrounding areas</h4>
      <div class="lead"><p>With over 15 years experience in the field of carpentry, joinery and attic loft conversions, we have completed numerous successful attic loft conversion projects. We find that dealing with our clients direct we can understand their needs and requirements much better and deliver a dream attic loft conversion. We are available at every stage of your london Loft Conversion to advise and explain your individual options. As a london loft conversion is a large project we like to make sure you end up with the best possible solution.</p></div>
      <div class="quote-disc">CLICK<br>HERE FOR<br>A <b>FREE</b><br>QUOTE</div>
      <h4>Examples of our London Loft Conversions</h4>
      <p>Please look at our london loft conversions galleries so you can examine the quality of our work. We would also be happy to take you personally to visit one of many of our happy customers to see their london loft conversions. We also have a video that you can view to show a attic loft conversion from start to finish. <a>Click here to view some of our london loft conversions.</a></p>
      <h4>London Loft Conversions Guarantees</h4>
      <p>All of our london loft conversions come with a 10 year guarantee.</p>
      <h4>London Loft Conversions Technical Information</h4>
      <ul>
        <li>Structural stability</li><li>Fire safety</li><li>Sound insulation</li><li>Ventilation of rooms and roofs</li><li>Sanitary facilities and drainage</li><li>Stairs and guarding</li><li>Thermal insulation</li>
      </ul>
      <h4>Need Financial help with your London Loft Conversion Project</h4>
      <p>If you would like us to help you with financing your attic loft conversion please fill in the contact form and we will call you to discuss.</p>
      <p><a>Click here to arrange a no obligation london loft conversion assessment.</a></p>
    </div>
    <aside class="side-col">
      <h2 class="sec">Customer <span>Testimonial</span></h2>
      <div class="testi">
        <q>I would like to thank you for the excellent standard of service and work when completing our attic loft conversion last year.</q>
        <p class="who">Laurent, Enfield</p>
        <q>I could not be more pleased with the way my attic loft conversion has been finished the quality of work is absolutely fantastic.</q>
        <p class="who">Chris, Enfield</p>
        <q>Dealing with you and your team, has been a pleasure, we are very pleased with the finished product.</q>
        <p class="who last">Tony, Waltham</p>
      </div>
      <h2 class="sec">Free <span>Survey</span></h2>
      <div class="field">Name</div>
      <div class="field tall">Address</div>
      <div class="field">Email</div>
      <div class="field">Phone</div>
      <div style="margin:9px 0 0 10px"><span class="btn small">Submit</span></div>
    </aside>
  </div>
</section>
<section class="band" style="height:305px">
  <div class="wrap">
    <div class="col c1">
      <h2 class="sec"><span>Visit Our</span> <em>Showroom</em></h2>
      <div class="thumb" role="img" aria-label="Photograph of a dining room showroom"></div>
      <p>Lorem ipsum dolor sit amet, consectetur adipiscing elit. Proin eget neque sapien. Vivamus tincidunt lectus sit amet nunc convallis et luctus mi posuere. Nunc varius pulvinar mauris, nec mattis ipsum varius a. Aliquam ac magna ligula. Nulla convallis accumsan rutrum.</p>
      <span class="btn">Read More</span>
    </div>
    <div class="col c2">
      <h2 class="sec"><em>Unrivelled</em> <span>After Support</span></h2>
      <div class="van" role="img" aria-label="Illustration of a white service van"></div>
      <p>Lorem ipsum dolor sit amet, consectetur adipiscing elit. Proin eget neque sapien. Vivamus tincidunt lectus sit amet nunc convallis et luctus mi posuere. Nunc varius pulvinar mauris, nec mattis ipsum varius a. Aliquam ac magna ligula.</p>
      <span class="btn">Read More</span>
    </div>
    <div class="col c3">
      <h2 class="sec"><span>Contact</span> <em>Information</em></h2>
      <div class="contact-body">
        <div class="phone-ic" role="img" aria-label="Illustration of a telephone handset with coiled cord"></div>
        <h3>GableNest</h3>
        <p>18 Larkfield Road<br>Enfield<br>Middlesex<br>EN2 9QX</p>
        <p class="em">Email us @</p>
        <p><a>sales@gablenest.example</a><br><a>aftersales@gablenest.example</a></p>
      </div>
    </div>
  </div>
</section>
<footer class="site-footer short">
  <div class="wrap">
    <div class="footer-links">Home<i>|</i>Technical Information<i>|</i>Gallery<i>|</i>Testimonials<i>|</i>Contact Us<i>|</i>Location</div>
    <div class="copy">© 2010 GableNest. All rights reserved.</div>
  </div>
</footer>

</body>
</html>
```